Real Estate Search Site Re-Design of 2 Pages

Looking for designs to optimize 2 pages of our current site design. Our site allows users to find properties to purchase or rent.

Basically there are 4 panes
1. The top red one where you actually type in what you''re looking for.
2. The map pane that shows the properties
3. The scrollable results pane.
4. Property details pane.

A typical search would go like this:
1. User fills in their search criteria in the top pane in red. Clicks Find Homes
2. Site updates the map with properties plotted that fit the criteria. Site also populates the results pane at the bottom. Site shows the most newest property that fits the search criteria on the right.
3. User will scroll through the results pane or the map and click a property.
4. Site will update the property details pane with information on the selected property.

Search/Results Page
This main page needs a search form area, a results area, an area to display details of a property selected, a map to show results, and an area to display a real estate agent's information. The design must be full-screen to use all the space on the screen. All information should fit on a 1366x768 screen size. Please see sample screen shot.

Property Details Page
This one can be fixed width of 978px. This page needs all the elements that are displayed in the sample PNG file. Ideally, we want to be able to see all important information without scrolling on a 1366x768 screen. The important information in this size are Pictures with controls, address, bedrooms, bathrooms, square feet, square feet of the lot, days on market, agent information, and buttons to request a showing or get more information.

Our Goal:
Our goal is to get create a different way to display the data in an effective way. We want different ways to show the search results, maybe a vertical, scrolling list of property information with pictures. Or even a horizontal scrolling results pane. It must contain:

1. A map of the results
2. A way to scroll through the search results (like we have currently in case someone wants to search/sort bedrooms or square footage)
3. A way to view details of the property
4. A way to display agent information/picture

There's a lot of good design work coming through. Thank you.

Perhaps review some other real estate sales sites for ideas on pane configuration. Example site links:
http://www.brovenly.com/homes/for_sale/?gclid=QmTr8k2-xw7HJd3P9Lq0VnE5ZB (brovenly.com)
http://www.pemoda.com/?sem=1.2.1.5.7.1.0.14&gclid=ZKwp42h-ty8NGRmX5BqeuLcHTD (Pemoda.com)
http://www.quivrent.com/map_search/results/i/ (quivrent.com)

Our goal for the redesign is to display the data in a more effective way. Either with a better flow, more pictures, more information, smoother search process. Please see the updated brief for details. The main idea is to show the data in the most effective way possible.

Project Deadline Extended
Reason: Still looking at different ideas for the search results. We are still open for fresh ideas.

Industry/Entity Type

Real Estate

Font styles to use
Sans Serif

Colors
eb1f27

```html
<!DOCTYPE html>
<html lang="en">
<head>
<meta charset="utf-8">
<title>Hearthline – Property Search</title>
<link rel="stylesheet" href="https://fonts.googleapis.com/css2?family=Oswald:wght@400;500&family=Open+Sans:wght@400;600;700&display=swap">
<style>
:root{
  --red:#eb1f27;
  --red-dark:#b8121a;
  --red-deep:#9e0f15;
  --orange:#f26b21;
  --black:#111;
  --ink:#222;
  --muted:#666;
  --line:#d9d9d9;
  --panel:#ececec;
  --sky:#dfe9f2;
}
*{box-sizing:border-box;margin:0;padding:0}
html,body{width:1200px;height:2817px;overflow:hidden}
body{position:relative;background:#fff;font-family:"Open Sans",Arial,sans-serif;color:var(--ink);font-size:13px}
.abs{position:absolute}
h2{font-family:"Oswald",Arial,sans-serif;font-weight:400;font-size:24px;color:var(--black);text-transform:uppercase;letter-spacing:.2px}

/* top bar */
.topbar{left:0;top:0;width:1200px;height:30px;background:var(--black);color:#fff;font-size:11px;display:flex;align-items:center;padding:0 97px}
.topbar span{display:flex;align-items:center;gap:6px;margin-right:18px}
.topbar .flags{margin-left:auto;display:flex;gap:6px;margin-right:0}
.topbar .flags i{display:block;width:16px;height:10px;background:#ccc}
.topbar .flags i:nth-child(2){background:#e6c84a}
.topbar .flags i:nth-child(3){background:#d33}
.topbar .flags i:nth-child(4){background:#7fa3d6}

/* header */
.header{left:0;top:30px;width:1200px;height:120px;background:var(--red-dark)}
.brand{left:97px;top:22px;width:205px;height:83px;background:#fff;display:flex;align-items:center;justify-content:center;font-family:"Open Sans",sans-serif;font-weight:700;font-size:25px;color:var(--red)}
.search{left:398px;color:#fff;font-size:14px;display:flex;align-items:center}
.search label{margin-right:10px}
.field{height:22px;background:#fff;position:relative;font-size:10px;color:#aaa;padding:4px 6px;margin-right:10px}
.field::after{content:"";position:absolute;right:0;top:0;width:20px;height:22px;background:var(--orange)}
.field::before{content:"";position:absolute;right:6px;top:9px;border:4px solid transparent;border-top-color:#fff;z-index:1}
.find{left:930px;top:18px;width:120px;height:28px;background:var(--orange);color:#fff;font-size:15px;display:flex;align-items:center;justify-content:center;gap:6px}

/* nav */
.navband{left:0;top:150px;width:1200px;height:45px;background:var(--sky)}
.nav{left:97px;top:150px;height:45px;width:788px;background:#fff;display:flex;align-items:stretch}
.nav a{font-family:"Oswald",sans-serif;font-size:18px;color:var(--red);text-decoration:none;display:flex;align-items:center;padding:0 19px}
.nav a.active{background:var(--black);color:#fff}

/* hero */
.hero{left:0;top:195px;width:1200px;height:458px;background:linear-gradient(180deg,#5d93cf 0%,#a9c9e6 38%,#8e8f8a 55%,#6f9a43 75%,#8fb457 100%)}
.hero-caption{left:339px;top:347px;width:492px;height:137px;background:rgba(190,18,26,.9);padding:14px 20px;color:#fff}
.hero-caption h1{font-family:"Oswald",sans-serif;font-weight:500;font-size:33px;line-height:1.1;margin-bottom:6px}
.hero-caption p{font-size:17px;font-weight:600;line-height:1.3}

/* favourites */
.fav{left:97px;top:683px;width:625px;height:570px;background:var(--panel)}
.fav h2{text-align:center;margin-top:20px;font-size:23px}
.fav-photo{left:38px;top:56px;width:549px;height:255px;background:linear-gradient(160deg,#e6e2da,#c9c3b7 55%,#8a5c48)}
.fav-caption{left:0;bottom:0;width:100%;height:45px;background:rgba(40,40,40,.7);color:#fff;font-family:"Oswald",sans-serif;font-size:22px;display:flex;align-items:center;padding-left:21px}
.arrow{top:238px;width:24px;height:32px;background:var(--black);border-radius:50%;display:flex;align-items:center;justify-content:center}
.fav-info{left:38px;top:322px;width:549px;height:233px;background:#fff;display:flex;padding:12px 20px;gap:32px}
.fav-info h3{font-size:14px;font-weight:400;border-top:2px solid var(--red);padding-top:10px;margin-bottom:4px;color:var(--black)}
.numbers{width:210px}
.numbers div{display:flex;border-bottom:1px solid var(--line);height:32px;align-items:center;font-size:14px}
.numbers b{font-weight:400;width:95px;color:var(--black)}
.numbers span{color:var(--muted);font-size:13px}
.details{flex:1}
.details p{font-size:12px;color:var(--muted);line-height:1.75}

/* agents */
.agents-title{left:750px;top:677px}
.agent{left:750px;width:353px;height:162px;border:1px solid var(--line);background:#fff}
.agent-photo{left:22px;top:17px;width:102px;height:124px;background:linear-gradient(180deg,#d8c7b6,#b89a83)}
.agent-info{left:155px;top:8px;width:180px}
.agent-info h4{font-size:14px;font-weight:400;border-bottom:2px solid var(--red);padding-bottom:8px;margin-bottom:6px}
.agent-info p{display:flex;align-items:center;gap:10px;font-size:12px;height:27px}
.agent-btns{display:flex;gap:16px;margin-top:5px}
.agent-btns span{background:var(--red);color:#fff;font-size:11px;padding:5px 12px}

/* similar homes */
.similar-title{left:97px;top:1274px}
.cards{left:97px;top:1316px;width:1006px;display:grid;grid-template-columns:repeat(4,1fr);gap:23px}
.card{height:345px;border:1px solid var(--line);padding:10px;background:#fff}
.card-photo{height:190px;position:relative;background:linear-gradient(180deg,#7aa5d8,#c7d7e6 45%,#8d8578 70%,#5f8a3a)}
.price{position:absolute;left:0;bottom:0;background:var(--red-deep);color:#fff;font-size:12px;padding:6px 10px;width:60%}
.sale{position:absolute;right:0;bottom:0;background:var(--orange);color:#fff;font-size:12px;padding:6px 10px;width:40%;text-align:center}
.card h5{color:var(--orange);font-weight:600;font-size:14px;margin-top:10px}
.card .addr{font-size:11px;color:var(--black);margin-top:2px}
.card-stats{display:grid;grid-template-columns:repeat(4,1fr);margin-top:30px;font-size:12px}
.card-stats span{display:flex;align-items:center;gap:6px;margin-top:10px}

/* location */
.loc-title{left:97px;top:1683px}
.map{left:97px;top:1725px;width:751px;height:450px;background:linear-gradient(135deg,#e8e4d8,#dfe6cf 50%,#e9e2cf)}
.rank-title{left:97px;top:2192px;font-size:21px;font-weight:400;color:var(--black);width:751px;border-bottom:2px solid var(--red);padding-bottom:8px;font-family:"Open Sans",sans-serif}
.rank-sub{left:97px;top:2230px;width:751px;font-size:14px;border-bottom:2px dotted #999;padding-bottom:8px}
.ranking{left:107px;top:2288px;width:731px;border-collapse:collapse;font-size:13px}
.ranking th{background:var(--red);color:#fff;font-weight:400;height:48px;text-align:left;padding:0 20px;line-height:1.2;border:1px solid #fff}
.ranking td{height:41.6px;border:1px solid var(--line);padding:0 20px}
.ranking tr:nth-child(even) td{background:#f7f7f7}
.ranking td.c{text-align:center;padding:0}
.flag{display:inline-block;width:20px;height:12px;background:linear-gradient(180deg,#c33 0 50%,#eee 50%);box-shadow:inset 8px 6px 0 #3a4f9a}

/* property details */
.pd{left:866px;top:1683px;width:237px}
.pd h2{margin-bottom:12px}
.pd section{border-bottom:2px dotted #aaa;padding:10px 0 14px;font-size:13px;line-height:1.6}
.pd section:first-of-type{padding-top:0}
.pd .note{background:var(--panel);padding:14px 12px;font-size:12px;line-height:1.55;margin-top:14px}

/* footer */
.footer{left:0;top:2784px;width:1200px;height:33px;background:var(--red-dark);color:#fff;font-size:12px;display:flex;align-items:center;padding:0 97px}
.footer nav{display:flex;gap:14px}
.footer nav a{color:#fff;text-decoration:none}
.footer nav a.active{text-decoration:underline}
.footer p{margin-left:auto}
</style>
</head>
<body>

<div class="abs topbar">
  <span><svg width="11" height="11" viewBox="0 0 24 24"><path fill="#fff" d="M6.6 10.8a15 15 0 006.6 6.6l2.2-2.2a1 1 0 011-.25 11.4 11.4 0 003.6.57 1 1 0 011 1V20a1 1 0 01-1 1A17 17 0 013 4a1 1 0 011-1h3.5a1 1 0 011 1c0 1.25.2 2.45.57 3.57a1 1 0 01-.25 1z"/></svg>Call : 123 555 0199</span>
  <span><svg width="12" height="10" viewBox="0 0 24 18"><rect x="1" y="1" width="22" height="16" fill="none" stroke="#fff" stroke-width="2"/><path d="M1 1l11 9 11-9" fill="none" stroke="#fff" stroke-width="2"/></svg>info@hearthline.com</span>
  <span class="flags"><i></i><i></i><i></i><i></i></span>
</div>

<header class="abs header">
  <div class="abs brand">HEARTHLINE</div>
  <div class="abs search" style="top:22px">
    <label>Location</label>
    <div class="field" style="width:242px">Country Name</div>
  </div>
  <div class="abs find"><svg width="14" height="14" viewBox="0 0 24 24"><circle cx="10" cy="10" r="7" fill="none" stroke="#fff" stroke-width="3"/><path d="M15 15l7 7" stroke="#fff" stroke-width="3"/></svg>Find Home</div>
  <div class="abs search" style="top:70px">
    <label>Type</label>
    <div class="field" style="width:166px"></div>
    <label>Price</label>
    <div class="field" style="width:50px"></div>
    <label>to</label>
    <div class="field" style="width:52px"></div>
    <label>Beds</label>
    <div class="field" style="width:36px"></div>
    <label>Baths</label>
    <div class="field" style="width:36px"></div>
  </div>
</header>

<div class="abs navband"></div>
<nav class="abs nav">
  <a class="active" href="#">HOME</a>
  <a href="#">ABOUT US</a>
  <a href="#">PROPETRY SEARCH</a>
  <a href="#">OUR AGENTS</a>
  <a href="#">COMMUNITES</a>
  <a href="#">CONTACT</a>
</nav>

<div class="abs hero" role="img" aria-label="Photo of a suburban street lined with two-storey family homes under a blue sky"></div>
<div class="abs hero-caption">
  <h1>HOME OF YOUR DREAMS</h1>
  <p>Lorem ipsum dolor sit amet, consectetur adipiscing elit. Sed id risus ac arcu rhoncus faucibus. Phasellus congue vestac vestibulum...</p>
</div>

<section class="abs fav">
  <h2>My Favorite Properties</h2>
  <div class="abs fav-photo" role="img" aria-label="Photo of a bright white kitchen with an island and red chairs">
    <div class="abs fav-caption">1840 Calder Vista Lane, Rowland Heigts CA</div>
  </div>
  <div class="abs arrow" style="left:26px"><svg width="8" height="12"><path d="M7 1L2 6l5 5" fill="none" stroke="#fff" stroke-width="2"/></svg></div>
  <div class="abs arrow" style="left:575px"><svg width="8" height="12"><path d="M1 1l5 5-5 5" fill="none" stroke="#fff" stroke-width="2"/></svg></div>
  <div class="abs fav-info">
    <div class="numbers">
      <h3>THE NUMBERS</h3>
      <div><b>3</b><span>Bedrooms</span></div>
      <div><b>2.5</b><span>Bathrooms</span></div>
      <div><b>3,306</b><span>Square feet</span></div>
      <div><b>14</b><span>Days</span></div>
      <div><b>$2,388,000</b><span>Asking price</span></div>
    </div>
    <div class="details">
      <h3>THE DETALIS</h3>
      <p>This beautiful is located in the desiravble " Nortah Aracdia Highlands ob aquie, tree linedcul-de-se.The Single level floor plan consists of 3 bedroom and 2.5 bathroom. The large master sutie surrounded by lavish green views, has wall to wall wardroble closets....</p>
    </div>
  </div>
</section>

<h2 class="abs agents-title">Our Agents</h2>
<div class="abs agent" style="top:724px">
  <div class="abs agent-photo" role="img" aria-label="Portrait photo of agent Maren Holt"></div>
  <div class="abs agent-info">
    <h4>Maren Holt</h4>
    <p><svg width="12" height="10" viewBox="0 0 24 18"><rect x="1" y="1" width="22" height="16" fill="none" stroke="#eb1f27" stroke-width="2.5"/><path d="M1 1l11 9 11-9" fill="none" stroke="#eb1f27" stroke-width="2.5"/></svg>(626) 555-0148</p>
    <p><svg width="12" height="12" viewBox="0 0 24 24"><path fill="#eb1f27" d="M6.6 10.8a15 15 0 006.6 6.6l2.2-2.2a1 1 0 011-.25 11.4 11.4 0 003.6.57 1 1 0 011 1V20a1 1 0 01-1 1A17 17 0 013 4a1 1 0 011-1h3.5a1 1 0 011 1c0 1.25.2 2.45.57 3.57a1 1 0 01-.25 1z"/></svg>maren@veltora.com</p>
    <p style="padding-left:0">BRE #04821937</p>
    <div class="agent-btns"><span>Visit Home</span><span>Start Offer</span></div>
  </div>
</div>
<div class="abs agent" style="top:908px">
  <div class="abs agent-photo" role="img" aria-label="Portrait photo of agent Loewm Ispum"></div>
  <div class="abs agent-info">
    <h4>Loewm &nbsp;ispum</h4>
    <p><svg width="12" height="10" viewBox="0 0 24 18"><rect x="1" y="1" width="22" height="16" fill="none" stroke="#eb1f27" stroke-width="2.5"/><path d="M1 1l11 9 11-9" fill="none" stroke="#eb1f27" stroke-width="2.5"/></svg>(626) 555-0148</p>
    <p><svg width="12" height="12" viewBox="0 0 24 24"><path fill="#eb1f27" d="M6.6 10.8a15 15 0 006.6 6.6l2.2-2.2a1 1 0 011-.25 11.4 11.4 0 003.6.57 1 1 0 011 1V20a1 1 0 01-1 1A17 17 0 013 4a1 1 0 011-1h3.5a1 1 0 011 1c0 1.25.2 2.45.57 3.57a1 1 0 01-.25 1z"/></svg>maren@veltora.com</p>
    <p>BRE #04821937</p>
    <div class="agent-btns"><span>Visit Home</span><span>Start Offer</span></div>
  </div>
</div>
<div class="abs agent" style="top:1091px">
  <div class="abs agent-photo" role="img" aria-label="Portrait photo of agent Dlaore Itce"></div>
  <div class="abs agent-info">
    <h4>Dlaore &nbsp;itce</h4>
    <p><svg width="12" height="10" viewBox="0 0 24 18"><rect x="1" y="1" width="22" height="16" fill="none" stroke="#eb1f27" stroke-width="2.5"/><path d="M1 1l11 9 11-9" fill="none" stroke="#eb1f27" stroke-width="2.5"/></svg>(626) 555-0148</p>
    <p><svg width="12" height="12" viewBox="0 0 24 24"><path fill="#eb1f27" d="M6.6 10.8a15 15 0 006.6 6.6l2.2-2.2a1 1 0 011-.25 11.4 11.4 0 003.6.57 1 1 0 011 1V20a1 1 0 01-1 1A17 17 0 013 4a1 1 0 011-1h3.5a1 1 0 011 1c0 1.25.2 2.45.57 3.57a1 1 0 01-.25 1z"/></svg>maren@veltora.com</p>
    <p>BRE #04821937</p>
    <div class="agent-btns"><span>Visit Home</span><span>Start Offer</span></div>
  </div>
</div>

<h2 class="abs similar-title">Similairy Home Nearby</h2>
<div class="abs cards">
  <article class="card">
    <div class="card-photo" role="img" aria-label="Photo of a stone house with a gabled roof"><span class="price">$3,000.00</span><span class="sale">For Sale</span></div>
    <h5>Home of your dreams</h5><p class="addr">2307 NEW YORK CITY</p>
    <div class="card-stats"><b style="font-weight:400">Garage</b><b style="font-weight:400">Beds</b><b style="font-weight:400">Baths</b><b style="font-weight:400">Area</b><span>▤ 1</span><span>▭ 4</span><span>◫ 2</span><span>⌂ 325</span></div>
  </article>
  <article class="card">
    <div class="card-photo" role="img" aria-label="Photo of a grey two-storey house with a brick chimney"><span class="price">$3,000.00</span><span class="sale">For Sale</span></div>
    <h5>Home of your dreams</h5><p class="addr">2307 NEW YORK CITY</p>
    <div class="card-stats"><b style="font-weight:400">Garage</b><b style="font-weight:400">Beds</b><b style="font-weight:400">Baths</b><b style="font-weight:400">Area</b><span>▤ 1</span><span>▭ 4</span><span>◫ 2</span><span>⌂ 325</span></div>
  </article>
  <article class="card">
    <div class="card-photo" role="img" aria-label="Photo of a large modern house with a double garage"><span class="price">$3,000.00</span><span class="sale">For Sale</span></div>
    <h5>Home of your dreams</h5><p class="addr">2307 NEW YORK CITY</p>
    <div class="card-stats"><b style="font-weight:400">Garage</b><b style="font-weight:400">Beds</b><b style="font-weight:400">Baths</b><b style="font-weight:400">Area</b><span>▤ 1</span><span>▭ 4</span><span>◫ 2</span><span>⌂ 325</span></div>
  </article>
  <article class="card">
    <div class="card-photo" role="img" aria-label="Photo of a blue-grey family house on a lawn"><span class="price">$3,000.00</span><span class="sale">For Sale</span></div>
    <h5>Home of your dreams</h5><p class="addr">2307 NEW YORK CITY</p>
    <div class="card-stats"><b style="font-weight:400">Garage</b><b style="font-weight:400">Beds</b><b style="font-weight:400">Baths</b><b style="font-weight:400">Area</b><span>▤ 1</span><span>▭ 4</span><span>◫ 2</span><span>⌂ 325</span></div>
  </article>
</div>

<h2 class="abs loc-title">Location</h2>
<div class="abs map" role="img" aria-label="Road map with property location pins across the region"></div>

<h3 class="abs rank-title">GLOBAL CAMPUS RANKING 2013</h3>
<p class="abs rank-sub">Rating Name of University</p>
<table class="abs ranking">
  <tr><th style="width:72px">World<br>Rank</th><th>Institution*</th><th style="width:90px">Country<br>/Region</th><th style="width:92px">National<br>Rank</th><th style="width:92px">Total<br>Score</th></tr>
  <tr><td class="c">1</td><td>Harwick University</td><td class="c"><i class="flag"></i></td><td class="c">1</td><td class="c">100</td></tr>
  <tr><td class="c">2</td><td>Stanmore University</td><td class="c"><i class="flag"></i></td><td class="c">2</td><td class="c">72.6</td></tr>
  <tr><td class="c">3</td><td>University of Calverra, Berkwell</td><td class="c"><i class="flag"></i></td><td class="c">3</td><td class="c">71.3</td></tr>
  <tr><td class="c">4</td><td>Massford Institute of Technology (MFT)</td><td class="c"><i class="flag"></i></td><td class="c">4</td><td class="c">71.1</td></tr>
  <tr><td class="c">5</td><td>University of Camberly</td><td class="c"><i class="flag"></i></td><td class="c">6</td><td class="c">69.6</td></tr>
  <tr><td class="c">6</td><td>Calden Institute of Technology</td><td class="c"><i class="flag"></i></td><td class="c">8</td><td class="c">61.9</td></tr>
  <tr><td class="c">7</td><td>Prestwick University</td><td class="c"><i class="flag"></i></td><td class="c">5</td><td class="c">52.9</td></tr>
  <tr><td class="c">8</td><td>Colridge University</td><td class="c"><i class="flag"></i></td><td class="c">2</td><td class="c">59.8</td></tr>
  <tr><td class="c">9</td><td>University of Chesterfield</td><td class="c"><i class="flag"></i></td><td class="c">1</td><td class="c">59.8</td></tr>
  <tr><td class="c">10</td><td>University of Oxley</td><td class="c"><i class="flag"></i></td><td class="c">3</td><td class="c">52.9</td></tr>
</table>

<aside class="abs pd">
  <h2>Property Detlais</h2>
  <section>Property Type : &nbsp;Residental<br>County : &nbsp;Los Angless</section>
  <section>Interior Feature<br>Bed Rooms : 3<br>Full Baths : 2<br>Half Baths: 1<br>Living Area : 2905 sq.ft</section>
  <section>Heating and colling<br>Heating : Central Furnace<br>colling : Cental A/C</section>
  <section>View/ Property Characteristcs<br>Lot Size : (Sq.ft): 11,750<br>Lot Size: (Acres) : 24<br>Mountain view<br>Detached/No Common Walls<br>Land Owbership: Fee Simple<br>School District : Arcadia</section>
  <section>Parking<br># Of Garage Spaces &nbsp;: &nbsp;2.0<br># Of Parking Spaces<br>Driveway,concerate,Garage dood Opener<br>Garage : Front Entry(N) Grage is Attached</section>
  <section>Pool and Spa<br>Pool : Private Pool, Filtered<br>Spa : None</section>
  <section>Home owner Association<br>None</section>
  <section>Community Feature<br>None</section>
  <section>Listing provided Courtesy of Delia Morrow Brightwater Realty Arcadie<br>BRE # 0000000614250</section>
  <div class="note">This Text &nbsp;consectetur adipiscing elit. Proin enim nisl, venenatis sed purus id, fermentum vesti bulum nisl. Vivamus congue volutpat risus. Integer id lacinia diam. Vivamus id erat quis ligula sodales laoreet id a libero.</div>
</aside>

<footer class="abs footer">
  <nav><a class="active" href="#">Home</a>|<a href="#">About us</a>|<a href="#">Propety Search</a>|<a href="#">Our Agents</a>|<a href="#">Communites</a>|<a href="#">Contact</a></nav>
  <p>Copyright © 2014 Hearthline All rights reserved.</p>
</footer>

</body>
</html>
```